Fitness Equipment Repair Business Needs a Catchy New Business Card

We have an existing business card, however, it is quite plain and boring. We are expanding primarily in the commercial area (gyms, studios, apartment complexes etc). The business card will serve as eye candy to those managers/owners that can't be met for a face to face.
Originally I was planning for a brochure as well, but all of our information is better summarized on our website. (brasswheelservicing.ca).
I would like the card to match the colour scheme of the website and utilize the logo. It should have a professional clean feel to it, however, a little colouring outside the lines wouldn't hurt.
The example card is for my service technician (Corwin Haldane). If possible I would like to be able to edit the text to use for more than one person.

Industry/Entity Type

Appliance Repair

Contact Information for Business Card

Clean, crisp and professional but needs to be eye catching. Preferably using the black, white and red colour scheme matching the website. Double sided would be nice, but is not necessary.

Colors
ec1f27
ffffff
000000

Requirements
Must have
• Must be able to edit name, phone number and title to use for multiple people. Must show the company website (brasswheelservicing.ca).

```html
<!DOCTYPE html>
<html lang="en">
<head>
<meta charset="utf-8">
<title>Brass Wheel Servicing – Business Card</title>
<link href="https://fonts.googleapis.com/css2?family=Arvo:wght@400;700&display=swap" rel="stylesheet">
<style>
  :root {
    --red: #ec1f27;
    --white: #ffffff;
    --black: #000000;
    --ink: #1a1a1a;
    --rule: #555555;
    --stage: #2a2a2a;
  }
  * { margin: 0; padding: 0; box-sizing: border-box; }
  html, body { width: 1200px; height: 800px; overflow: hidden; }
  body {
    background: var(--stage);
    font-family: "Arvo", Georgia, serif;
    display: flex;
    align-items: center;
    justify-content: center;
    gap: 70px;
  }
  .card {
    width: 440px;
    height: 440px;
    border-radius: 34px;
    position: relative;
    overflow: hidden;
    box-shadow: 0 10px 30px rgba(0,0,0,.5);
  }

  /* Front */
  .card-front { background: var(--black); color: var(--white); }
  .front-band {
    position: absolute; left: 0; bottom: 0; height: 16px; width: 100%;
    display: flex;
  }
  .front-band .band-red { width: 46%; background: var(--red); }
  .front-band .band-white { width: 14%; background: var(--white); }
  .brand-mark {
    position: absolute; left: 0; right: 0; top: 120px;
    text-align: center;
    font-weight: 700; font-size: 34px; line-height: 1.15;
    color: var(--white);
  }
  .brand-line {
    position: absolute; left: 34px; bottom: 46px;
    font-size: 24px; font-variant: small-caps; letter-spacing: 2px;
    color: var(--white);
  }

  /* Back */
  .card-back { background: var(--white); color: var(--ink); }
  .back-band {
    position: absolute; left: 0; right: 0; bottom: 0; height: 64px;
    background: var(--red);
    border-top: 8px solid var(--black);
    display: flex; align-items: center; justify-content: center;
  }
  .website { color: var(--white); font-weight: 700; font-size: 19px; letter-spacing: .3px; }
  .contact {
    position: absolute; right: 40px; top: 40px; width: 330px;
    text-align: right;
  }
  .person-name { font-weight: 700; font-size: 30px; line-height: 1.1; }
  .person-title { color: var(--red); font-weight: 700; font-size: 20px; margin-bottom: 16px; }
  .address { font-weight: 700; font-size: 15px; line-height: 1.35; padding-bottom: 12px; border-bottom: 1px solid var(--rule); }
  .entry { padding: 7px 0; border-bottom: 1px solid var(--rule); }
  .entry:last-child { border-bottom: none; }
  .entry-label { color: var(--red); font-size: 10px; }
  .entry-value { font-weight: 700; font-size: 16px; }
</style>
</head>
<body>
  <section class="card card-front">
    <div class="brand-mark">Brass Wheel<br>Servicing</div>
    <div class="brand-line">Brass Wheel Servicing</div>
    <div class="front-band"><span class="band-red"></span><span class="band-white"></span></div>
  </section>

  <section class="card card-back">
    <div class="contact">
      <div class="person-name">Corwin Haldane</div>
      <div class="person-title">service technician</div>
      <div class="address">1875 Alder Cove NW<br>Edmonton AB T5K 2P8</div>
      <div class="entry"><div class="entry-label">Personal:</div><div class="entry-value">578-555-0142</div></div>
      <div class="entry"><div class="entry-label">Service Line:</div><div class="entry-value">780-555-0187</div></div>
      <div class="entry"><div class="entry-label">Service Email:</div><div class="entry-value">brasswheelsv@outlook.com</div></div>
    </div>
    <div class="back-band"><span class="website">www.brasswheelservicing.ca</span></div>
  </section>
</body>
</html>
```